Signage Design Project - Florida Vacation Resort Monument Sign

I need a design for the main identification sign outside of a resort in Florida. This is a sign that will be located at ground level near the entrance to the resort.

Text to include:

"4818" (This is the property address numbers, no street name necessary)

"Coral Haven" (This is the name of the resort)

"Heated Pool" (bullet point)
"Tiki Hut" (bullet point)
"Beach Access" (bullet point)

"Weekly/Monthly Rentals" (text to appear at bottom of sign)

Dimensions: 55.5"wide x 43.5"tall

Some design elements can protrude from the dimensions, as long as they are not too thin. It will ultimately need to be cut out of wood and if a design element is thin and sticks out of the box, it will be likely to break off.

***The artwork must be vectored.***

Please use whatever design elements you'd like in full color. A palm tree might make sense because of the name "Coral Haven", but I don't want to limit your creativity!

The website is here: http://www.coral-haven-example.com

They have a tour your can click on at the bottom for more pictures to get a feel for the property.

```html
<!DOCTYPE html>
<html lang="en">
<head>
<meta charset="utf-8">
<title>Coral Haven – Monument Sign</title>
<link rel="stylesheet" href="https://fonts.googleapis.com/css2?family=Arimo:wght@400;700&family=Archivo+Black&display=swap">
<style>
  :root {
    --sky: #7fd6f8;
    --cloud: #eeeeee;
    --sea: #14b4c6;
    --sand: #dde9a6;
    --numeral: #f8f5c0;
    --numeral-light: #fdfbe2;
    --numeral-shadow: #a39f7c;
    --board-top: #bdbdbd;
    --board-bottom: #8e8e8e;
    --board-edge: #e4e4e4;
    --lettering: #ffffff;
    --lettering-shadow: #a3121d;
  }
  html, body {
    margin: 0;
    padding: 0;
    overflow: hidden;
    background: var(--sky);
  }
  .sign-canvas {
    position: relative;
    width: 1200px;
    height: 940px;
    overflow: hidden;
  }
  .beach-scene {
    position: absolute;
    inset: 0;
    background: linear-gradient(180deg,
      var(--sky) 0%,
      var(--sky) 34%,
      var(--cloud) 48%,
      var(--cloud) 70%,
      var(--sea) 76%,
      var(--sea) 85%,
      var(--sand) 91%,
      var(--sand) 100%);
  }
  .address-numerals {
    position: absolute;
    left: 92px;
    top: -14px;
    margin: 0;
    font-family: "Arimo", Arial, sans-serif;
    font-weight: 700;
    font-size: 430px;
    line-height: 1;
    letter-spacing: 10px;
    background: linear-gradient(180deg, var(--numeral-light), var(--numeral));
    -webkit-background-clip: text;
    background-clip: text;
    -webkit-text-fill-color: transparent;
    filter: drop-shadow(-9px 6px 0 var(--numeral-shadow));
  }
  .sign-board {
    position: absolute;
    inset: 0;
    width: 1200px;
    height: 940px;
  }
  .board-lettering {
    position: absolute;
    left: 365px;
    top: 505px;
    width: 560px;
    height: 340px;
    transform: rotate(-9.5deg);
    transform-origin: left top;
    color: var(--lettering);
    text-shadow: -2px 3px 0 var(--lettering-shadow), -1px 1px 0 var(--lettering-shadow);
  }
  .board-lettering > * {
    position: absolute;
    margin: 0;
    white-space: nowrap;
    line-height: 1;
  }
  .resort-name {
    left: 0;
    top: 36px;
    font-family: "Archivo Black", "Arial Black", sans-serif;
    font-weight: 400;
    font-size: 62px;
    letter-spacing: 1px;
  }
  .amenities {
    list-style: none;
    padding: 0;
    left: 0;
    top: 0;
    font-family: "Arimo", Arial, sans-serif;
    font-size: 45px;
  }
  .amenities li {
    position: absolute;
    white-space: nowrap;
  }
  .amenities li::before {
    content: "•";
    margin-right: 2px;
  }
  .amenity-pool  { left: 70px; top: 108px; }
  .amenity-tiki  { left: 76px; top: 170px; }
  .amenity-beach { left: 82px; top: 228px; }
  .rental-terms {
    left: 28px;
    top: 300px;
    font-family: "Arimo", Arial, sans-serif;
    font-size: 27px;
    transform: rotate(2.5deg);
    transform-origin: left top;
  }
</style>
</head>
<body>
<main class="sign-canvas">
  <div class="beach-scene" role="img" aria-label="Illustrated beach scene with blue sky, white clouds, turquoise sea, sand, a wooden sign post and palm trees"></div>

  <p class="address-numerals">4818</p>

  <svg class="sign-board" viewBox="0 0 1200 940" xmlns="http://www.w3.org/2000/svg">
    <defs>
      <linearGradient id="board-fill" x1="0" y1="0" x2="0" y2="1">
        <stop offset="0" stop-color="var(--board-top)"/>
        <stop offset="1" stop-color="var(--board-bottom)"/>
      </linearGradient>
    </defs>
    <polygon points="860,417 872,424 930,790 918,792" fill="var(--board-edge)"/>
    <polygon points="310,510 860,417 918,792 333,852" fill="url(#board-fill)"/>
  </svg>

  <div class="board-lettering">
    <h1 class="resort-name">Coral Haven</h1>
    <ul class="amenities">
      <li class="amenity-pool">Heated Pool</li>
      <li class="amenity-tiki">Tiki Hut</li>
      <li class="amenity-beach">Beach Access</li>
    </ul>
    <p class="rental-terms">Weekly/Monthly Rentals</p>
  </div>
</main>
</body>
</html>
```